Fine Art business needs new website

We need a simple website with a home page, about us page, New sculptures, Sold sculptures, and a contact us page.Our sculptures are very high end one of a kind pieces. As such we need the site to be VERY elegant and professional. Lastly, because I'll be updating pictures on the website on a monthly basis it needs to be user friendly to update (Wordpress is preferred). The only branding we have so far for the business is a business card.
Updates
I wasn't completely ready when this project launched, also I am on the road right now and haven't been able to be as responsive to all you designers as I would like. I will work on giving feedback to all the top designs we've received so far. Thank you all so much for your participation and hardwork.
Target Market(s)
High end customers (affluent), art collectors, interior decorators/designers
Industry/Entity Type
Art Gallery
Coding
Coded - Design and coding required
Number of Pages Required
5+ page
Requirements
Must have
- Easily editable picture gallery for myself so that I can add new pieces(pictures of the pieces), remove sold pieces, etc. I would like the website to be built in wordpress so I can update it. I currently use sitekeeperpro through Netbirch for my other business website and would like to do the same for this one.
- Pages:
- -Intro page with featured pieces
- -Current pieces gallery (for sale) mainly a picture gallery
- -Sculptures archive (sold pieces) another picture gallery
- -About us: Pull-down of -about the artist (attached content)
- -Artistic Process (attached content)
- -Show Schedule:
- -one page dedicated to "friends of QMW" (basically a link page)
- TO BE CLEAR "www.lanternhollow.com" IS A TOTALLY DIFFERENT SITE AND I'M NOT TRYING TO COMBINE THE TWO OR JOIN THEM INTO ONE. This page needs be more elegant and seperate from the Lantern Hollow site.
- UPDATE: I'd like a link to the QMW Facebook page: https://www.facebook.com/quillmarkworks/
Nice to have
- I would like the pictures on the gallery pages able to have text connected with them (Materials, price)
- I would like the site style and fonts to be similar to our business cards we've already had designed (picture attached).
Should not have
- Too much flash or other things that will make the site slow to load.

```html
<!DOCTYPE html>
<html lang="en">
<head>
<meta charset="utf-8">
<title>About Us – Meet the Artists</title>
<link href="https://fonts.googleapis.com/css2?family=Lato:wght@400;700&family=Crimson+Text:wght@400;600&display=swap" rel="stylesheet">
<style>
:root{
  --ink:#222222;
  --ink-soft:#3a3a3a;
  --muted:#6a6a6a;
  --bar:#232323;
  --page:#f2f2f2;
  --page-light:#f8f8f8;
  --rule:#c9c9c9;
  --white:#ffffff;
  --accent:#8aa0c8;
  --social:#8c8c8c;
}
*{margin:0;padding:0;box-sizing:border-box}
html,body{width:740px;height:1200px;overflow:hidden}
body{position:relative;background:var(--page);font-family:"Lato",sans-serif;color:var(--ink)}
.abs{position:absolute}

/* top bar */
.top-bar{left:0;top:0;width:740px;height:46px;background:var(--bar);box-shadow:0 2px 4px rgba(0,0,0,.25);z-index:2}
.main-nav{left:116px;top:16px;display:flex;gap:13px;font-size:8.5px;color:var(--white);text-transform:uppercase;letter-spacing:.1px}
.main-nav .current{position:relative;display:flex;align-items:center;gap:4px}
.main-nav .current::after{content:"";position:absolute;left:-4px;right:-2px;top:14px;height:1px;background:var(--accent)}
.menu-toggle{left:602px;top:16px;width:22px;height:13px}
.dropdown{left:116px;top:35px;width:79px;height:38px;background:var(--white);box-shadow:1px 1px 3px rgba(0,0,0,.3);z-index:3;font-size:7.5px;color:var(--ink);padding:5px 0 0 12px;line-height:17.5px}

/* heading area */
.page-title{left:0;width:740px;top:76px;text-align:center;font-size:25px;font-weight:700;letter-spacing:-.3px}
.title-rule{left:321px;top:110px;width:98px;height:1.5px;background:var(--rule)}
.tab{top:136px;font-size:10.5px;font-weight:700;text-transform:uppercase}
.tab-active{left:249px;color:var(--ink)}
.tab-idle{left:396px;color:var(--muted)}
.tab-divider{left:369px;top:128px;width:1px;height:28px;background:#d6d6d6}
.section-title{left:0;width:740px;top:199px;text-align:center;font-size:17.5px;font-weight:400;letter-spacing:-.2px}
.section-rule{left:317px;top:227px;width:106px;height:1.5px;background:var(--rule)}

.photo{box-shadow:2px 2px 4px rgba(0,0,0,.35)}
.team-photo{left:257px;top:252px;width:226px;height:169px;background:linear-gradient(110deg,#b9b3a2 0%,#8e8a80 35%,#4f74b8 70%,#2f5fb0 100%)}

.story{left:155px;width:430px;top:439px;font-size:10.3px;line-height:16px;text-align:center;color:var(--ink-soft)}
.story p{margin-bottom:16px}

/* artists */
.artists-band{left:0;top:721px;width:740px;height:349px;background:var(--page-light)}
.artist-name{font-size:13.5px;font-weight:400;color:var(--ink)}
.bio-label{font-family:"Crimson Text",serif;font-size:11px;font-weight:600;color:var(--ink-soft)}
.bio-text{font-family:"Crimson Text",serif;font-size:9.6px;line-height:16px;color:#555}
.portrait-hal{left:117px;top:772px;width:170px;height:116px;background:linear-gradient(135deg,#9c8a6c 0%,#6d5c45 45%,#3b3430 100%)}
.portrait-wes{left:455px;top:928px;width:169px;height:116px;background:linear-gradient(180deg,#a9aab0 0%,#c9b9a8 45%,#5a4a3e 75%,#e6e9ee 100%)}

/* footer */
.site-footer{left:0;top:1070px;width:740px;height:130px;background:var(--bar);color:var(--white)}
.footer-heading{top:26px;font-size:13.5px;font-weight:700;text-transform:uppercase;letter-spacing:-.2px}
.footer-text{top:48px;font-size:7.5px;line-height:13.2px}
.contact-list{left:325px;top:48px;font-size:7.5px;line-height:13.2px;list-style:none}
.contact-list li{display:flex;align-items:center;gap:6px}
.contact-list svg{width:8px;height:8px}
.contact-link{font-weight:700;padding-left:14px;text-transform:uppercase}
.social{left:543px;top:50px;display:flex;gap:7px}
.social span{width:12px;height:12px;background:var(--social);display:block}
</style>
</head>
<body>

<header class="abs top-bar">
  <nav class="abs main-nav">
    <span>Home</span>
    <span class="current">About
      <svg width="7" height="5" viewBox="0 0 7 5"><path d="M.5 .8 3.5 3.8 6.5 .8" fill="none" stroke="#fff" stroke-width=".9"/></svg>
    </span>
    <span>Gallery</span>
    <span>Contact</span>
  </nav>
  <svg class="abs menu-toggle" viewBox="0 0 22 13"><rect y="0" width="22" height="1.8" fill="#fff"/><rect y="5.5" width="22" height="1.8" fill="#fff"/><rect y="11" width="22" height="1.8" fill="#fff"/></svg>
</header>
<div class="abs dropdown">
  <div>About the Artists</div>
  <div>The Lantern Hollow</div>
</div>

<h1 class="abs page-title">ABOUT US</h1>
<div class="abs title-rule"></div>

<div class="abs tab tab-active">Meet the Artists</div>
<div class="abs tab-divider"></div>
<div class="abs tab tab-idle">The Artistic Process</div>

<h2 class="abs section-title">MEET THE ARTISTS</h2>
<div class="abs section-rule"></div>

<div class="abs photo team-photo" role="img" aria-label="Photo of the two artists in the workshop wearing respirator masks"></div>

<div class="abs story">
  <p>Hal Brenner has been mastering the Lapidary Arts since the late 1980’s. Somewhere in the middle of this new career of his he recruited his kids into the shop to help him with the ever increasing demand for his one of a kind fossil and mineral sculptures. An unintended (or possibly intended) consequence of bringing his children into the fold is they eventually fell in love with rocks and became proficient in many of the lapidary techniques.</p>
  <p>Fast forward to 2012, after graduating college and working several years in the real world two of Hal’s children, Wesley and Nora, decided to work with their Father full-time as a chance to be closer to family while at the same time seeing different parts of the US. Through the past 6 years all of Hal’s children have continued to contribute to the family livelihood on a part-time basis with the exception of Wes who is now a full time Artist alongside his Father.</p>
  <p>Both Hal and Wes have their own unique styles, yet<br>on occasion they will combine their talents to create a collaborative masterpiece.</p>
</div>

<section class="abs artists-band">
  <div class="abs artist-name" style="left:117px;top:25px">Harold “Hal” Brenner</div>
  <div class="abs bio-label" style="left:305px;top:85px">Biography</div>
  <div class="abs bio-text" style="left:305px;top:105px;width:300px">“To learn more about the process of creating these one-of-a-kind sculptures please visit the Artistic process page of the website.”</div>

  <div class="abs artist-name" style="left:460px;width:164px;text-align:right;top:176px">Wes Brenner</div>
  <div class="abs bio-label" style="left:300px;width:135px;text-align:right;top:243px">Biography</div>
  <div class="abs bio-text" style="left:142px;width:300px;text-align:right;top:262px">“To learn more about the process of creating these one-of-a-kind sculptures please visit the Artistic process page of the website.”</div>
</section>

<div class="abs photo portrait-hal" role="img" aria-label="Portrait of Hal Brenner outdoors in a brown hat"></div>
<div class="abs photo portrait-wes" role="img" aria-label="Portrait of Wes Brenner in a snowy backyard at dusk"></div>

<footer class="abs site-footer">
  <div class="abs footer-heading" style="left:122px">About Us</div>
  <div class="abs footer-text" style="left:121px;width:135px">This is a dummy text just<br>to provide text in the About Us<br>section which will be added correctly<br>later on.</div>

  <div class="abs footer-heading" style="left:325px">Our Address</div>
  <ul class="abs contact-list">
    <li><svg viewBox="0 0 8 8"><path d="M1.6.5 2.9 2 2.2 3c.5 1.2 1.5 2.2 2.7 2.7l1-.7L7.5 6.4 6.6 7.5C3.6 7.3.7 4.4.5 1.4Z" fill="#fff"/></svg>(555) 013-2940</li>
    <li><svg viewBox="0 0 8 8"><rect x=".5" y="1.5" width="7" height="5" fill="none" stroke="#fff" stroke-width=".8"/><path d="M.5 1.5 4 4.5 7.5 1.5M.5 6.5 3 4M7.5 6.5 5 4" fill="none" stroke="#fff" stroke-width=".7"/></svg>wes@quillmarkworks.com</li>
    <li><svg viewBox="0 0 8 8"><path d="M3.4 4.6 4.6 3.4M2.8 3.4 1.6 4.6a1.3 1.3 0 0 0 1.8 1.8L4.6 5.2M5.2 4.6 6.4 3.4A1.3 1.3 0 0 0 4.6 1.6L3.4 2.8" fill="none" stroke="#fff" stroke-width=".8"/></svg>www.quillmarkworks.com</li>
    <li class="contact-link">Contact Us</li>
  </ul>

  <div class="abs footer-heading" style="left:526px">Keep in Touch</div>
  <div class="abs social">
    <span aria-label="Social profile 1"></span>
    <span aria-label="Social profile 2"></span>
    <span aria-label="Social profile 3"></span>
    <span aria-label="Social profile 4"></span>
  </div>
</footer>

</body>
</html>
```